Birchline Heating & Air

I need a business card made for my company. I would like my new logo for Birchline Heating and Air on the front and my Garage Door on the back.
Front to say -Heating & Air Conditioning , Mini Splits and Heat Pumps, Hydronic In-Floor Heat. Locally Owned and Operated! Licensed, Boned and Insured. Free Estimates on new equipment. 715-408-2159
BGD Back Card, change phone# to 651-374-5810. Remove Commercial and residential and fully sticked vans lines.

```html
<!DOCTYPE html>
<html lang="en">
<head>
<meta charset="utf-8">
<title>Birchline Heating &amp; Air — Business Cards</title>
<link href="https://fonts.googleapis.com/css2?family=Lato:wght@400;700;900&display=swap" rel="stylesheet">
<style>
  :root {
    --blue: #0f5189;
    --red: #f02a12;
    --white: #ffffff;
    --ink: #1d1d1f;
    --stage: #3a3a3c;
  }
  * { box-sizing: border-box; margin: 0; padding: 0; }
  html, body { width: 1200px; height: 875px; overflow: hidden; }
  body {
    background: var(--stage);
    font-family: 'Lato', sans-serif;
    position: relative;
  }
  .card {
    position: absolute;
    top: 283px;
    width: 540px;
    height: 309px;
    background: var(--white);
    border-radius: 18px;
    overflow: hidden;
  }
  .card--front { left: 40px; }
  .card--back { left: 620px; }

  /* Front */
  .front-logo {
    position: absolute;
    top: 34px; left: 0; right: 0;
    text-align: center;
    color: var(--red);
    font-weight: 900;
    font-size: 40px;
    letter-spacing: 1px;
    text-transform: uppercase;
    line-height: 1;
  }
  .front-logo .sub {
    display: block;
    font-size: 26px;
    margin-top: 6px;
    letter-spacing: 3px;
  }
  .service-band {
    position: absolute;
    top: 130px; left: 0; right: 0;
    height: 62px;
    background: var(--blue);
    color: var(--white);
    font-weight: 700;
    font-size: 12.5px;
    text-align: center;
    display: flex;
    flex-direction: column;
    justify-content: center;
    gap: 5px;
  }
  .front-offer {
    position: absolute;
    top: 206px; left: 0; right: 0;
    text-align: center;
    color: var(--red);
  }
  .front-offer .note { font-weight: 700; font-size: 14px; }
  .front-offer .phone { font-weight: 900; font-size: 46px; line-height: 1.1; letter-spacing: 1px; }

  /* Back */
  .back-logo {
    position: absolute;
    top: 36px; right: 34px;
    color: var(--blue);
    font-weight: 900;
    font-size: 22px;
    text-transform: uppercase;
    text-align: right;
    line-height: 1.15;
    letter-spacing: 1px;
  }
  .back-rule {
    position: absolute;
    top: 118px; left: 200px; right: 34px;
    height: 2px;
    background: var(--red);
  }
  .person { position: absolute; top: 132px; left: 34px; }
  .person .name {
    color: var(--blue);
    font-weight: 900;
    font-size: 27px;
    letter-spacing: 3px;
    text-transform: uppercase;
    white-space: nowrap;
  }
  .person .role { color: var(--red); font-size: 15px; margin-top: 2px; }
  .call {
    position: absolute;
    top: 200px; left: 34px;
    display: flex; align-items: center; gap: 10px;
  }
  .call .label { color: var(--blue); font-weight: 900; font-size: 13px; letter-spacing: 0.5px; }
  .call .phone { color: var(--red); font-weight: 900; font-size: 26px; line-height: 1; }
  .web {
    position: absolute;
    top: 212px; right: 34px;
    display: flex; align-items: center; gap: 10px;
    font-size: 12.5px; color: var(--ink);
    line-height: 1.35;
  }
  .web strong { font-weight: 900; }
  .footer-band {
    position: absolute;
    bottom: 0; left: 0; right: 0;
    height: 38px;
  }
  .footer-band .left, .footer-band .right {
    position: absolute; top: 0; bottom: 0;
    display: flex; align-items: center;
    color: var(--white); font-size: 12.5px;
    white-space: nowrap;
  }
  .footer-band .left {
    left: 0; width: 72%;
    background: var(--blue);
    padding-left: 34px;
    clip-path: polygon(0 0, 100% 0, 96% 100%, 0 100%);
  }
  .footer-band .right {
    right: 0; width: 31%;
    background: var(--red);
    justify-content: center;
    padding-left: 14px;
    font-size: 12px;
    clip-path: polygon(10% 0, 100% 0, 100% 100%, 0 100%);
  }
</style>
</head>
<body>
  <section class="card card--front" aria-label="Front of business card">
    <div class="front-logo">Birchline<span class="sub">Heating &amp; Air</span></div>
    <div class="service-band">
      <p>Heating &amp; Air Conditioning | Mini Splits &amp; Heat Pumps | Hydronic In-Floor Heat</p>
      <p>Locally Owned &amp; Operated! | Licensed, Boned &amp; Insured.</p>
    </div>
    <div class="front-offer">
      <p class="note">Free Estimates on new equipment.</p>
      <p class="phone">715-408-2159</p>
    </div>
  </section>

  <section class="card card--back" aria-label="Back of business card">
    <div class="back-logo">Birchline<br>Garage Door</div>
    <div class="back-rule"></div>
    <div class="person">
      <p class="name">Dana Whitford</p>
      <p class="role">Founder &amp; CEO</p>
    </div>
    <div class="call">
      <svg width="28" height="28" viewBox="0 0 24 24" aria-hidden="true">
        <path fill="#0f5189" d="M6.6 10.8a15.1 15.1 0 0 0 6.6 6.6l2.2-2.2a1 1 0 0 1 1-.25 11.4 11.4 0 0 0 3.6.57 1 1 0 0 1 1 1V20a1 1 0 0 1-1 1A17 17 0 0 1 3 4a1 1 0 0 1 1-1h3.5a1 1 0 0 1 1 1c0 1.25.2 2.45.57 3.6a1 1 0 0 1-.25 1z"/>
      </svg>
      <div>
        <p class="label">FREE SERVICE CALL</p>
        <p class="phone">651-374-5810</p>
      </div>
    </div>
    <div class="web">
      <svg width="26" height="26" viewBox="0 0 24 24" aria-hidden="true">
        <circle cx="12" cy="12" r="10" fill="none" stroke="#0f5189" stroke-width="2"/>
        <ellipse cx="12" cy="12" rx="4" ry="10" fill="none" stroke="#0f5189" stroke-width="1.6"/>
        <path d="M2 12h20M4 7h16M4 17h16" stroke="#0f5189" stroke-width="1.4"/>
      </svg>
      <div>
        <p>birchlinegaragedoor@mailbox.com</p>
        <p>www.<strong>birchlinegaragedoor</strong>.com</p>
      </div>
    </div>
    <div class="footer-band">
      <div class="left">Same Day &amp; Emergency Service | All Major Brands</div>
      <div class="right">Locally Owned &amp; Operated</div>
    </div>
  </section>
</body>
</html>
```